Logo for Internal Medicine practice

I want a logo for my Internal Medicine practice, I would like it to be with my name on it which is Lucía Barrenechea Ruiz.

I would like the business card to say the following (it is in Spanish since my practice is in Spanish):

Lucía Barrenechea Ruiz
Medicina Interna
Cel. 5583617204
luciabarrenechearuiz@correovela.mx

Logo Text

Lucía Barrenechea

```html
<!DOCTYPE html>
<html lang="es">
<head>
<meta charset="utf-8">
<title>Lucía Barrenechea Ruiz — Tarjeta de presentación</title>
<link rel="stylesheet" href="https://fonts.googleapis.com/css2?family=Montserrat:wght@400;500;800&display=swap">
<style>
  :root {
    --bg: #4a4a4a;
    --card: #141414;
    --card-back: #0e0e0e;
    --pattern-light: #2a2a2a;
    --pattern-mid: #181818;
    --pattern-dark: #050505;
    --red: #e52228;
    --blue: #4a8fd4;
    --white: #f2f2f2;
  }
  * { margin: 0; padding: 0; box-sizing: border-box; }
  html, body { width: 1200px; height: 801px; overflow: hidden; }
  body {
    background: var(--bg);
    font-family: "Montserrat", sans-serif;
    position: relative;
  }
  .card {
    position: absolute;
    top: 246px;
    width: 540px;
    height: 309px;
    border-radius: 16px;
    overflow: hidden;
    border-bottom: 4px solid var(--red);
    box-shadow: 0 18px 40px rgba(0,0,0,.45);
  }
  .card--front { left: 40px; background: var(--card); }
  .card--back { left: 620px; background: var(--card-back); }

  .front__tab {
    position: absolute;
    left: 0; bottom: 0;
    width: 26px; height: 34px;
    background: var(--red);
    border-top-right-radius: 8px;
  }
  .contact {
    position: absolute;
    left: 46px; bottom: 24px;
    color: var(--white);
    font-size: 12px;
    line-height: 1.45;
  }
  .contact__name {
    color: var(--red);
    font-weight: 800;
    font-size: 21px;
    line-height: 1.1;
  }
  .contact__role { font-size: 13px; margin-bottom: 14px; }
  .contact__address { margin-bottom: 14px; }
  .contact__line { display: flex; align-items: center; gap: 7px; }
  .contact__line svg { width: 11px; height: 11px; flex: none; }

  .brand {
    position: absolute;
    right: 32px; top: 30px;
    display: flex;
    flex-direction: column;
    align-items: flex-end;
    gap: 10px;
  }
  .brand__dot {
    width: 30px; height: 30px;
    border-radius: 50%;
    background: var(--blue);
  }
  .brand__name {
    color: var(--red);
    font-weight: 800;
    font-size: 18px;
    line-height: 1;
    text-transform: uppercase;
    letter-spacing: .5px;
  }

  .back__pattern {
    position: absolute;
    inset: 0;
    background:
      radial-gradient(ellipse at 18% 70%, var(--pattern-light) 0%, transparent 45%),
      radial-gradient(ellipse at 45% 30%, #222 0%, transparent 40%),
      linear-gradient(120deg, var(--pattern-mid) 0%, #101010 50%, var(--pattern-dark) 100%);
  }
  .back__brand {
    position: absolute;
    right: 44px; top: 118px;
    display: flex;
    flex-direction: column;
    align-items: flex-end;
    gap: 10px;
  }
  .back__brand .brand__dot { width: 40px; height: 40px; }
  .back__brand .brand__name { font-size: 16px; }
</style>
</head>
<body>
  <section class="card card--front">
    <div class="front__tab"></div>
    <div class="brand">
      <span class="brand__dot"></span>
      <span class="brand__name">Lucía Barrenechea</span>
    </div>
    <div class="contact">
      <p class="contact__name">Lucía Barrenechea Ruiz</p>
      <p class="contact__role">Medicina Interna</p>
      <p class="contact__address">1187 Calle Alameda Norte<br>Valle Sereno CA 90417</p>
      <p class="contact__line">
        <svg viewBox="0 0 12 12" aria-hidden="true"><rect x="3" y="0.5" width="6" height="11" rx="1" fill="none" stroke="#e52228" stroke-width="1.2"/></svg>
        5583617204
      </p>
      <p class="contact__line">
        <svg viewBox="0 0 12 12" aria-hidden="true"><rect x="0.5" y="2.5" width="11" height="7" fill="#e52228"/><path d="M0.5 2.5 6 7 11.5 2.5" fill="none" stroke="#141414" stroke-width="1"/></svg>
        luciabarrenechearuiz@correovela.mx
      </p>
      <p class="contact__line">
        <svg viewBox="0 0 12 12" aria-hidden="true"><circle cx="6" cy="6" r="5.5" fill="#e52228"/><path d="M1 6h10M6 .5v11" stroke="#141414" stroke-width=".8"/></svg>
        www.consultoriovela.mx
      </p>
    </div>
  </section>

  <section class="card card--back">
    <div class="back__pattern" role="img" aria-label="Tonal black embossed repeating pattern covering the whole card back"></div>
    <div class="back__brand">
      <span class="brand__dot"></span>
      <span class="brand__name">Lucía Barrenechea</span>
    </div>
  </section>
</body>
</html>
```